BRIVETTA Need a luxury modern business card designed.

Need a luxury modern business card designed. refer to the uploaded files for the company name and logo in the zip file under source files. i will making my descion on monday. so please send in before then so if we need to edit we will have the time. we have a trade show coming up and im on a deadline for printer.

Target Market(s)

high end clients

Contact Information for Business Card

Company nAme and logo. Calvin Moross Co-Founder / Project Manager Office # 416-555-7391 Cell # 416-555-0186 BRIVETTA.CA Calvin@brivetta.ca

Font styles to use
Other font styles liked:
• Modern

Requirements
Must have
• Company name and logo, contact info, using the black, gold and white color scheme.

```html
<!DOCTYPE html>
<html lang="en">
<head>
<meta charset="utf-8">
<title>Brivetta Business Card</title>
<link href="https://fonts.googleapis.com/css2?family=Josefin+Sans:wght@300;400&family=Raleway:wght@700&family=Open+Sans:wght@400&display=swap" rel="stylesheet">
<style>
  :root {
    --backdrop: #5d5d5d;
    --card-light: #ffffff;
    --card-dark: #333333;
    --gold: #a39561;
    --ink: #222222;
    --rule: #9a9a9a;
    --muted: #8a8a8a;
  }
  html, body {
    margin: 0;
    padding: 0;
    width: 1200px;
    height: 900px;
    overflow: hidden;
    background: var(--backdrop);
  }
  .canvas {
    position: relative;
    width: 1200px;
    height: 900px;
  }
  .card {
    position: absolute;
    top: 200px;
    width: 310px;
    height: 502px;
    box-sizing: border-box;
  }
  .card--front {
    left: 253px;
    background: var(--card-light);
    border-radius: 70px 0 70px 0;
  }
  .card--back {
    left: 627px;
    background: var(--card-dark);
    border-radius: 0 70px 0 70px;
  }
  .brand {
    position: absolute;
    left: 0;
    width: 100%;
    text-align: center;
  }
  .brand__mark {
    display: block;
    width: 12px;
    height: 12px;
    margin: 0 auto 22px;
    background: var(--gold);
  }
  .brand__name {
    font-family: "Josefin Sans", sans-serif;
    font-weight: 300;
    font-size: 31px;
    letter-spacing: 5px;
    line-height: 1;
    padding-left: 5px;
  }
  .brand__tagline {
    display: flex;
    align-items: center;
    justify-content: center;
    gap: 7px;
    margin-top: 6px;
    font-family: "Josefin Sans", sans-serif;
    font-weight: 400;
    font-size: 9px;
    letter-spacing: 2.4px;
  }
  .brand__tagline::before,
  .brand__tagline::after {
    content: "";
    width: 22px;
    height: 1px;
    background: currentColor;
  }
  .card--front .brand { top: 146px; }
  .card--front .brand__name { color: var(--ink); }
  .card--front .brand__tagline { color: var(--muted); }
  .card--back .brand { top: 258px; }
  .card--back .brand__name { color: #ffffff; }
  .card--back .brand__tagline { color: #ffffff; }

  .person {
    position: absolute;
    left: 42px;
    top: 335px;
  }
  .person__name {
    font-family: "Raleway", sans-serif;
    font-weight: 700;
    font-size: 17px;
    color: var(--gold);
    letter-spacing: 0.3px;
    margin: 0;
  }
  .person__role {
    font-family: "Open Sans", sans-serif;
    font-size: 13px;
    color: var(--ink);
    margin: 3px 0 0;
  }
  .contacts {
    position: absolute;
    left: 42px;
    top: 397px;
    margin: 0;
    padding: 0;
    list-style: none;
    font-family: "Open Sans", sans-serif;
    font-size: 13px;
    color: var(--ink);
  }
  .contacts__item {
    display: flex;
    align-items: center;
    gap: 5px;
    height: 18px;
  }
  .contacts__icon {
    width: 13px;
    height: 13px;
    fill: var(--gold);
    flex: none;
  }
</style>
</head>
<body>
<main class="canvas">
  <section class="card card--front">
    <div class="brand">
      <span class="brand__mark"></span>
      <div class="brand__name">BRIVETTA</div>
      <div class="brand__tagline">LUXURY LANDSCAPES</div>
    </div>
    <div class="person">
      <p class="person__name">CALVIN MOROSS</p>
      <p class="person__role">Co-Founder / Project Manager</p>
    </div>
    <ul class="contacts">
      <li class="contacts__item">
        <svg class="contacts__icon" viewBox="0 0 14 14" aria-hidden="true"><path d="M1 5c0-2 2-3 6-3s6 1 6 3v1h-3V5H4v1H1z"/><path d="M3 7h8l1 5H2z"/></svg>
        416-555-7391
      </li>
      <li class="contacts__item">
        <svg class="contacts__icon" viewBox="0 0 14 14" aria-hidden="true"><path d="M4 0h6a1 1 0 0 1 1 1v12a1 1 0 0 1-1 1H4a1 1 0 0 1-1-1V1a1 1 0 0 1 1-1zm0.5 1.5v9h5v-9zM7 11.3a0.9 0.9 0 1 0 0 1.8a0.9 0.9 0 1 0 0-1.8z"/></svg>
        416-555-0186
      </li>
      <li class="contacts__item">
        <svg class="contacts__icon" viewBox="0 0 14 14" aria-hidden="true"><path d="M1 3h12v1L7 8 1 4z"/><path d="M1 5.2l6 4 6-4V11H1z"/></svg>
        brivetta.ca calvin@brivetta.ca
      </li>
    </ul>
  </section>

  <section class="card card--back">
    <div class="brand">
      <span class="brand__mark"></span>
      <div class="brand__name">BRIVETTA</div>
      <div class="brand__tagline">LUXURY LANDSCAPES</div>
    </div>
  </section>
</main>
</body>
</html>
```